Crimson Covenant (Vampire, Werewolf, and Witch factions)

A beautiful landing page.
A header image, displayed on all web pages.
Item images for each of the players to be able to equip to their accounts.
Housing images, which players will live in.
And advertising banners.

The theme for this game is vampires, werewolves, and witches, and all the images should resemble this!

This is for a web/text based game. If you have any further questions feel free to message me!
If you are interested, we can get into details on what items we will be looking for, and housing types we want.

Font styles to use
Sans Serif

Colors
6c459b
886aae
ec1f27
000000
1b1b1b
757575
333333
f04a51

Requirements
Must have
• Landing
• Header image
• Item images
• Housing images
• Advertising banners.
Nice to have
• Include vampires, werewolves and witches in the landing and header/advertising banners.

```html
<!DOCTYPE html>
<html lang="en">
<head>
<meta charset="utf-8">
<title>Crimson Covenant – Vampire</title>
<link rel="stylesheet" href="https://fonts.googleapis.com/css2?family=Cinzel:wght@400;700;900&family=Merriweather:wght@400&family=Noto+Sans:wght@400&display=swap">
<style>
  :root {
    --page-bg: #191c26;
    --panel: #3a3150;
    --panel-line: #aaa2bd;
    --content-bg: #c4a8e6;
    --ink-dark: #1b1b2a;
    --ink-light: #ffffff;
    --ad-text: #886aae;
    --social: #f04a51;
    --black: #000000;
  }
  * { box-sizing: border-box; margin: 0; padding: 0; }
  html, body { width: 1200px; height: 1108px; overflow: hidden; }
  body {
    position: relative;
    background: var(--page-bg);
    font-family: "Noto Sans", sans-serif;
    color: var(--ink-light);
  }
  .profile-card {
    position: absolute; left: 60px; top: 2px; width: 249px; height: 323px;
    background: var(--panel); border: 1px solid var(--panel-line); border-radius: 8px;
  }
  .profile-avatar {
    position: absolute; left: 31px; top: 20px; width: 185px; height: 142px; border-radius: 8px;
    background: radial-gradient(circle at 50% 40%, #6e5f7e 0%, #3a3244 45%, #1e1b26 100%);
  }
  .profile-nav {
    position: absolute; left: 31px; top: 188px; list-style: none;
    font-family: "Cinzel", serif; font-size: 17px; line-height: 27px; font-variant: small-caps;
  }
  .site-header {
    position: absolute; left: 335px; top: 0; width: 803px; height: 323px; border-radius: 6px;
    border: 1px solid #2a2d38;
    background:
      radial-gradient(ellipse at 45% 45%, rgba(120,110,150,.45) 0%, rgba(0,0,0,0) 45%),
      radial-gradient(ellipse at 78% 55%, rgba(130,128,145,.55) 0%, rgba(0,0,0,0) 40%),
      linear-gradient(90deg, #3c4050 0%, #2a2c38 40%, #0a0f18 100%);
  }
  .side-menu {
    position: absolute; left: 60px; top: 353px; width: 249px; height: 591px;
    background: var(--panel); border: 1px solid var(--panel-line); border-radius: 8px;
    list-style: none; text-align: center;
    font-family: "Cinzel", serif; font-weight: 700; font-size: 28px; font-variant: small-caps;
  }
  .side-menu li { position: absolute; left: 0; width: 100%; }
  .content {
    position: absolute; left: 338px; top: 353px; width: 617px; height: 591px;
    background: var(--content-bg); border-radius: 8px; border: 1px solid #b49ad2;
    color: var(--ink-dark);
  }
  .content-title {
    position: absolute; left: 0; top: 44px; width: 100%; text-align: center;
    font-family: "Cinzel", serif; font-weight: 700; font-size: 28px; font-variant: small-caps;
  }
  .content-body { position: absolute; left: 51px; top: 136px; width: 560px; font-size: 14.5px; line-height: 20px; }
  .content-body p + p { margin-top: 20px; }
  .ad-slot {
    position: absolute; background: var(--panel); border: 3px solid var(--black);
    display: flex; align-items: center; justify-content: center;
    font-family: "Merriweather", serif; font-size: 21px; color: var(--ad-text);
  }
  .ad-skyscraper { left: 992px; top: 353px; width: 148px; height: 553px; }
  .ad-leaderboard { left: 337px; top: 966px; width: 672px; height: 83px; }
  .follow-title {
    position: absolute; left: 60px; top: 958px; width: 226px; text-align: center;
    font-family: "Cinzel", serif; font-weight: 700; font-size: 28px; font-variant: small-caps;
  }
  .social-list {
    position: absolute; left: 60px; top: 1016px; width: 250px; list-style: none;
    display: flex; justify-content: space-between;
    font-family: "Cinzel", serif; font-weight: 700; font-size: 15px; color: var(--social);
  }
  .copyright {
    position: absolute; left: 0; top: 1066px; width: 1304px; text-align: center; font-size: 20px;
  }
</style>
</head>
<body>
  <aside class="profile-card">
    <div class="profile-avatar" role="img" aria-label="Player avatar: vampire character portrait"></div>
    <ul class="profile-nav">
      <li>Name</li>
      <li>Messages</li>
      <li>Progress</li>
      <li>Train</li>
    </ul>
  </aside>

  <header class="site-header" role="img" aria-label="Header artwork: vampire in front of a night-time castle with drifting mist"></header>

  <ul class="side-menu">
    <li style="top:34px">Menu item 1</li>
    <li style="top:121px">Menu item 2</li>
    <li style="top:208px">Menu item 3</li>
  </ul>

  <main class="content">
    <h1 class="content-title">Vampire</h1>
    <div class="content-body">
      <p>Lorem ipsum dolor sit amet, te per commodo corrumpit,<br>et eos nostrud placerat. Sit graeco ponderum te, eirmod<br>blandit his ne. Vis id dignissim pertinacia. Iracundia repudiandae<br>te has, noster facilis eu vel. Et vel ignota doming, ius ut tritani p<br>ercipit detraxit. Accumsan deleniti fabellas ut vis, eos et eirmod<br>adipiscing scribentur, ne probatus incorrupte vix. Quodsi interpretaris<br>conclusionemque ex mel.</p>
      <p>Dolor aliquid deseruisse cum an, pro ei vitae officiis. No quo nemore<br>constituto inciderint. Pro at gubergren referrentur, ea hinc nominavi<br>consequuntur sit, cu delicata corrumpit scriptorem vis. Dico sensibus<br>gubergren cu eum. An meliore assueverit pro, malis fuisset eu pri. Cu<br>vix corpora percipit. Erant suavitate vis ut, te vel corpora efficiantur.</p>
      <p>Partem labitur et sit, mea cu autem possim expetendis. Sed ad labores<br>utroque appareat. Nec novum putant equidem ne. Vis ei posse admodum,<br>ludus quando inimicus qui at. Cum an ludus fuisset reprehendunt.<br>Nec quot fastidii ex, est ad modo oblique oportere. Eos id quod noluisse<br>temporibus, ex est nobis disputando, te ius eruditi molestiae.</p>
    </div>
  </main>

  <div class="ad-slot ad-skyscraper">160x600px</div>

  <h2 class="follow-title">Follow us</h2>
  <ul class="social-list">
    <li>Fang</li>
    <li>Howl</li>
    <li>Moon</li>
    <li>Coven</li>
  </ul>

  <div class="ad-slot ad-leaderboard">728x90px</div>

  <footer class="copyright">© copyright</footer>
</body>
</html>
```